Tulven Electrics Flyer Design Advertising

I am after an A5 Flyer design to help promote my electrical services business.
I would like to have information on what my business offers, photos of electrical work, and specials/deals for an amount of time.

Industry/Entity Type

Electrician

Font styles to use
Sans Serif

Colors
0292cd
33a6d7
85cae6
3176b5
333333
1b1b1b
ffffff
5c5c5c
474747

Requirements
Must have
• Specialising in New homes, renovations and commercial projects
• Contact details:
• ph. 0437 619 458
• email admin@tulvenelectrics.example.au
• facebook TulvenElectrics
• Specials/Deals:
• 10% off all electrical services
• or
• Free LED downlights on installation
• *Terms conditions apply
• ALL RESIDENTIAL & COMMERCIAL ELECTRICAL SERVICES
• - New Home installations
• - Commercial projects
• - Shop fit outs
• - Renovations
• - Smoke Detectors
• - Air Conditioning and Ceiling Fans
• - Garden Lighting
• - Oven and Cooktop Installations
• - Power Point installation
• - LED lighting upgrades
• - Security Lighting
• - Switchboard upgrades
• - Test and Tag
• - Commercial Property
• - General Electrical Maintenance

```html
<!DOCTYPE html>
<html lang="en">
<head>
<meta charset="utf-8">
<title>Tulven Electrics Flyer</title>
<link href="https://fonts.googleapis.com/css2?family=Oswald:wght@500;600&family=Open+Sans:ital,wght@0,400;0,700;0,800;1,800&family=Roboto:ital,wght@0,700;0,900;1,900&display=swap" rel="stylesheet">
<style>
:root{
  --blue:#0292cd;
  --blue-mid:#33a6d7;
  --blue-light:#85cae6;
  --blue-deep:#3176b5;
  --navy:#0d4f9e;
  --ink:#333333;
  --black:#1b1b1b;
  --white:#ffffff;
  --grey:#5c5c5c;
  --grey-dark:#474747;
  --paper:#e9eaec;
  --paper-top:#eeeeef;
}
*{margin:0;padding:0;box-sizing:border-box}
html,body{width:897px;height:1200px;overflow:hidden;background:#f2f2f2}
.flyer{position:relative;width:897px;height:1200px;background:var(--paper);font-family:"Open Sans",Arial,sans-serif;color:var(--ink);overflow:hidden}
.backdrop{position:absolute;inset:0}
.brand{position:absolute;left:38px;top:23px;display:flex;align-items:center;gap:14px}
.brand-dot{width:164px;height:164px;border-radius:50%;background:var(--blue)}
.brand-name{position:absolute;left:50px;top:52px;font-family:"Open Sans",Arial,sans-serif;font-weight:800;font-size:46px;line-height:1;color:var(--grey-dark);white-space:nowrap;letter-spacing:1px}
.services-tab{position:absolute;left:0;top:784px;width:439px;height:60px;background:linear-gradient(90deg,var(--blue),var(--navy));border-radius:0 22px 22px 0;padding:9px 0 0 35px;color:var(--white);font-family:"Roboto",Arial,sans-serif;font-weight:900;font-size:19px;line-height:24px;letter-spacing:.3px}
.specialising{position:absolute;left:35px;top:862px;font-family:"Roboto",Arial,sans-serif;font-style:italic;font-weight:900;font-size:16.5px;color:var(--grey-dark);white-space:nowrap}
.service-list{position:absolute;top:906px;list-style:none;font-size:18px;line-height:29px;color:var(--ink)}
.service-list li{position:relative;padding-left:25px;white-space:nowrap}
.service-list li::before{content:"";position:absolute;left:0;top:8px;width:14px;height:14px;border-radius:50%;background:var(--blue)}
.service-list li::after{content:"";position:absolute;left:4px;top:12px;width:4px;height:4px;border-right:2px solid var(--white);border-top:2px solid var(--white);transform:rotate(45deg)}
.list-left{left:35px}
.list-right{left:357px}
.offer{position:absolute;left:687px;width:184px;height:148px;border-radius:14px;background:#cfd0d2;overflow:hidden;text-align:center;box-shadow:0 2px 3px rgba(0,0,0,.12)}
.offer-main{height:118px;background:linear-gradient(135deg,var(--blue) 0%,var(--blue-deep) 55%,var(--navy) 100%);color:var(--white);padding-top:14px;border-bottom-right-radius:14px}
.offer-big{font-family:"Oswald",Arial,sans-serif;font-weight:600;font-size:44px;line-height:50px;letter-spacing:1px}
.offer-small{font-family:"Roboto",Arial,sans-serif;font-weight:700;font-size:14.5px;line-height:20px;letter-spacing:.8px}
.offer-terms{font-size:12px;line-height:30px;color:var(--grey)}
.offer-one{top:786px}
.offer-two{top:948px}
.offers-end{position:absolute;left:687px;width:184px;top:1101px;text-align:center;font-size:12px;color:var(--grey)}
.footer-phone{position:absolute;left:38px;top:1138px;display:flex;align-items:center;gap:22px;color:var(--white)}
.footer-phone span{font-family:"Oswald",Arial,sans-serif;font-weight:500;font-size:44px;line-height:1;letter-spacing:.5px}
.footer-contact{position:absolute;right:18px;top:1136px;text-align:right;color:var(--white);font-size:17.5px;line-height:30px}
.footer-contact div{display:flex;align-items:center;justify-content:flex-end;gap:12px}
.footer-contact .plain-circle{width:22px;height:22px;border-radius:50%;background:var(--white)}
</style>
</head>
<body>
<div class="flyer">
  <svg class="backdrop" width="897" height="1200" viewBox="0 0 897 1200" xmlns="http://www.w3.org/2000/svg">
    <defs>
      <linearGradient id="kitchenTone" x1="0" y1="0" x2="1" y2="1">
        <stop offset="0" stop-color="#3d3f44"/>
        <stop offset=".35" stop-color="#c9c3b8"/>
        <stop offset=".7" stop-color="#ddd6ca"/>
        <stop offset="1" stop-color="#9b9690"/>
      </linearGradient>
      <linearGradient id="gardenTone" x1="0" y1="0" x2="0" y2="1">
        <stop offset="0" stop-color="#2b3a3e"/>
        <stop offset=".5" stop-color="#e2d7c8"/>
        <stop offset="1" stop-color="#6d4b30"/>
      </linearGradient>
      <linearGradient id="poolTone" x1="0" y1="0" x2="0" y2="1">
        <stop offset="0" stop-color="#8fa3bd"/>
        <stop offset=".5" stop-color="#7b7168"/>
        <stop offset="1" stop-color="#3ab3cf"/>
      </linearGradient>
      <linearGradient id="houseTone" x1="0" y1="0" x2="0" y2="1">
        <stop offset="0" stop-color="#5d88c4"/>
        <stop offset=".55" stop-color="#b7b2a8"/>
        <stop offset="1" stop-color="#3f6b2c"/>
      </linearGradient>
      <linearGradient id="footerBlue" x1="0" y1="0" x2="1" y2="0">
        <stop offset="0" stop-color="#0292cd"/>
        <stop offset="1" stop-color="#0d4f9e"/>
      </linearGradient>
    </defs>

    <rect x="0" y="0" width="897" height="300" fill="var(--paper-top)"/>
    <polygon points="0,240 897,86 897,100 0,262" fill="var(--grey-dark)"/>
    <polygon points="0,262 897,100 0,300" fill="var(--blue)"/>

    <polygon role="img" aria-label="Photo of a modern kitchen with pendant lights and island bench" points="0,300 897,100 897,560 0,680" fill="url(#kitchenTone)"/>

    <polygon points="0,662 430,602 430,614 0,684" fill="var(--blue)"/>
    <polygon points="430,602 897,538 897,562 430,626" fill="var(--grey-dark)"/>

    <g class="photo-circle">
      <path d="M167,550 A104,104 0 0 0 167,758" fill="none" stroke="var(--blue)" stroke-width="8"/>
      <path d="M167,550 A104,104 0 0 1 167,758" fill="none" stroke="#a9a9ad" stroke-width="8"/>
      <circle role="img" aria-label="Photo of an outdoor lounge lit by wall and deck lights" cx="167" cy="654" r="98" fill="url(#gardenTone)" stroke="var(--white)" stroke-width="3"/>
    </g>
    <g class="photo-circle">
      <path d="M448,508 A104,104 0 0 0 448,716" fill="none" stroke="var(--blue)" stroke-width="8"/>
      <path d="M448,508 A104,104 0 0 1 448,716" fill="none" stroke="#a9a9ad" stroke-width="8"/>
      <circle role="img" aria-label="Photo of a modern house with lit pool at dusk" cx="448" cy="612" r="98" fill="url(#poolTone)" stroke="var(--white)" stroke-width="3"/>
    </g>
    <g class="photo-circle">
      <path d="M742,466 A104,104 0 0 0 742,674" fill="none" stroke="var(--blue)" stroke-width="8"/>
      <path d="M742,466 A104,104 0 0 1 742,674" fill="none" stroke="#a9a9ad" stroke-width="8"/>
      <circle role="img" aria-label="Photo of a weatherboard home with exterior lighting" cx="742" cy="570" r="98" fill="url(#houseTone)" stroke="var(--white)" stroke-width="3"/>
    </g>

    <polygon points="0,1127 472,1127 442,1200 0,1200" fill="url(#footerBlue)"/>
    <polygon points="476,1127 482,1127 452,1200 446,1200" fill="var(--white)"/>
    <polygon points="486,1127 897,1127 897,1200 456,1200" fill="var(--grey-dark)"/>
  </svg>

  <div class="brand">
    <div class="brand-dot"></div>
    <div class="brand-name">Tulven Electrics</div>
  </div>

  <div class="services-tab">ALL RESIDENTIAL &amp; COMMERCIAL<br>ELECTRICAL SERVICES</div>
  <p class="specialising">SPECIALISING IN NEW HOMES, RENOVATIONS &amp; COMMERCIAL PROJECTS</p>

  <ul class="service-list list-left">
    <li>New Home installations</li>
    <li>Commercial projects</li>
    <li>Shop fit outs</li>
    <li>Renovations</li>
    <li>Smoke Detectors</li>
    <li>Garden Lighting</li>
    <li>Oven and Cooktop Installations</li>
  </ul>
  <ul class="service-list list-right">
    <li>Power Point installation</li>
    <li>LED lighting upgrades</li>
    <li>Security Lighting</li>
    <li>Switchboard upgrades</li>
    <li>Test and Tag</li>
    <li>Commercial Property</li>
    <li>General Electrical Maintenance</li>
  </ul>

  <div class="offer offer-one">
    <div class="offer-main">
      <div class="offer-big">10% OFF</div>
      <div class="offer-small">ALL ELECTRICAL<br>SERVICES</div>
    </div>
    <div class="offer-terms">*Terms conditions apply</div>
  </div>
  <div class="offer offer-two">
    <div class="offer-main">
      <div class="offer-big">FREE LED</div>
      <div class="offer-small">DOWNLIGHTS ON<br>INSTALLATION</div>
    </div>
    <div class="offer-terms">*Terms conditions apply</div>
  </div>
  <p class="offers-end">Offers end 30/11/18</p>

  <div class="footer-phone">
    <svg width="46" height="46" viewBox="0 0 46 46" aria-hidden="true">
      <circle cx="23" cy="23" r="20" fill="none" stroke="var(--white)" stroke-width="3"/>
      <path d="M15,13 l5,-2 l3,7 l-3,2 q2,5 6,7 l2,-3 l7,3 l-2,5 q-12,1 -18,-19z" fill="var(--white)"/>
    </svg>
    <span>0437 619 458</span>
  </div>

  <div class="footer-contact">
    <div>admin@tulvenelectrics.example.au
      <svg width="22" height="22" viewBox="0 0 22 22" aria-hidden="true">
        <circle cx="11" cy="11" r="11" fill="var(--white)"/>
        <rect x="5" y="7" width="12" height="8" fill="var(--grey-dark)"/>
        <path d="M5,7 l6,5 l6,-5" fill="none" stroke="var(--white)" stroke-width="1.3"/>
      </svg>
    </div>
    <div>TulvenElectrics <span class="plain-circle"></span></div>
  </div>
</div>
</body>
</html>
```